Tri-fold Brochure for Law Firm

Double-sided brochure to be folded into 6 sides tri-fold brochure for an estate planning special for new parents or parents-to-be. Brochure will be placed in classes for new parents/young parents.

Target Market(s)

New Parents Aged 24-34

Industry/Entity Type

Law Firm

Font styles to use
Serif

Requirements
Must have
• The information provided in the word document.
Nice to have
• Highlight the phrase "for New Parents."
• You may use the color scheme from our website:
• http://k47.9dw.sitevaultexample.com/

```html
<!DOCTYPE html>
<html lang="en">
<head>
<meta charset="utf-8">
<title>Estate Planning Special for New Parents – Tri-fold Brochure</title>
<link rel="stylesheet" href="https://fonts.googleapis.com/css2?family=Playfair+Display:wght@700;900&family=Montserrat:wght@600;700&family=Open+Sans:wght@400;600&display=swap">
<style>
  :root {
    --brown: #3a3129;
    --gold: #f0b92f;
    --slate: #5b5a58;
    --paper: #ffffff;
    --ink: #2d2a27;
    --backdrop: #e4e4e0;
    --serif: "Playfair Display", Georgia, serif;
    --head: "Montserrat", Arial, sans-serif;
    --body: "Open Sans", Arial, sans-serif;
  }
  * { box-sizing: border-box; margin: 0; padding: 0; }
  html, body { width: 1200px; height: 1200px; overflow: hidden; background: var(--backdrop); }
  .sheet {
    position: absolute; left: 230px; width: 740px; height: 572px;
    background: var(--paper); box-shadow: 0 4px 18px rgba(0,0,0,.18); overflow: hidden;
  }
  .sheet--outside { top: 20px; }
  .sheet--inside { top: 608px; }
  .panel { position: absolute; top: 0; width: 246.67px; height: 572px; overflow: hidden; }
  .panel--1 { left: 0; }
  .panel--2 { left: 246.67px; }
  .panel--3 { left: 493.33px; }
  .shapes { position: absolute; inset: 0; width: 100%; height: 100%; }
  .photo { position: absolute; left: 0; width: 100%; }
  .txt { position: absolute; font-family: var(--body); color: var(--ink); }

  /* outside: promo panel */
  .photo--writing { top: 0; height: 300px; background: linear-gradient(160deg, #5d5a57 0%, #a08a73 45%, #d7d2cc 100%); }
  .promo { left: 26px; top: 322px; width: 196px; }
  .promo h3 { font-family: var(--head); font-weight: 700; font-size: 12px; line-height: 1.3; }
  .promo p { font-size: 9.5px; line-height: 1.45; margin-top: 2px; }

  /* outside: attorney panel */
  .attorney-bg { position: absolute; left: 0; top: 0; width: 100%; height: 330px; background: var(--brown); }
  .portrait { position: absolute; left: 48px; top: 26px; width: 150px; height: 150px; background: linear-gradient(180deg, #8a8580 0%, #6e4a3e 60%, #7a2a34 100%); }
  .quote { left: 30px; top: 196px; width: 190px; color: var(--gold); font-size: 9.3px; line-height: 1.45; }
  .attorney-name { left: 30px; top: 300px; color: #fff; font-size: 10.5px; }
  .firm { left: 0; top: 368px; width: 100%; text-align: center; }
  .firm-name { display: flex; justify-content: center; align-items: center; gap: 7px; font-family: var(--serif); font-weight: 900; font-size: 13px; letter-spacing: .5px; color: var(--ink); }
  .firm-name .mark { width: 10px; height: 10px; background: var(--gold); }
  .firm p { font-size: 8.6px; line-height: 1.35; margin-top: 2px; }
  .firm .address { margin-top: 8px; }

  /* outside: cover */
  .cover-bg { position: absolute; inset: 0; background: var(--brown); }
  .photo--family { top: 0; height: 290px; background: linear-gradient(180deg, #d9d6d2 0%, #b9a593 55%, #8c7e73 100%); }
  .cover-title { left: 0; top: 402px; width: 100%; text-align: center; }
  .cover-title h1 { font-family: var(--serif); font-weight: 900; font-size: 17px; line-height: 1.2; color: var(--gold); letter-spacing: .3px; }
  .cover-title h1 .highlight { display: inline-block; font-size: 19px; }
  .cover-title p { margin-top: 4px; font-size: 8.5px; color: #fff; font-weight: 600; }

  /* inside: why a will */
  .photo--scales { top: 0; height: 212px; background: linear-gradient(135deg, #6b3d1c 0%, #c07a35 45%, #e7b56a 70%, #7b4a22 100%); }
  .why { left: 26px; top: 226px; width: 200px; }
  .why h3, .later h3 { font-family: var(--head); font-weight: 700; font-size: 11.5px; line-height: 1.25; color: var(--ink); }
  .why p, .later p, .laws-intro p { font-size: 9.2px; line-height: 1.45; margin-top: 6px; }
  .why h3 + p { margin-top: 6px; }
  .why p + h3 { margin-top: 12px; }

  /* inside: middle */
  .laws-intro { left: 22px; top: 16px; width: 205px; }
  .laws-intro p:first-child { margin-top: 0; }
  .laws-callout { left: 28px; top: 222px; width: 192px; font-family: var(--head); font-weight: 600; font-size: 12.5px; line-height: 1.3; color: var(--ink); }
  .later { left: 22px; top: 392px; width: 205px; }
  .call { left: 0; top: 547px; width: 100%; text-align: center; font-family: var(--head); font-weight: 700; font-size: 13px; color: #fff; }
  .call .label { color: var(--gold); margin-right: 6px; }

  /* inside: process */
  .photo--signing { top: 0; height: 160px; background: linear-gradient(160deg, #f4f2ee 0%, #d8d4ce 55%, #b9a99a 100%); }
  .process { left: 22px; top: 176px; width: 206px; color: #fff; }
  .process h3 { font-family: var(--head); font-weight: 700; font-size: 11.5px; line-height: 1.25; color: var(--gold); }
  .process p { font-size: 9.1px; line-height: 1.45; margin-top: 5px; color: #fff; }
  .process p + h3 { margin-top: 12px; }
</style>
</head>
<body>

<!-- Outside of the sheet: back, mailing panel, cover -->
<section class="sheet sheet--outside">
  <article class="panel panel--1">
    <div class="photo photo--writing" role="img" aria-label="Photo of a parent signing documents at a desk"></div>
    <svg class="shapes" viewBox="0 0 247 572" preserveAspectRatio="none" aria-hidden="true">
      <polygon points="0,302 247,268 247,572 0,572" fill="#fff"/>
      <polygon points="247,470 247,572 118,572" fill="var(--gold)"/>
    </svg>
    <div class="txt promo">
      <h3>New Parent Estate Planning program ends 12/31/17.</h3>
      <p>Special does not apply to individuals with over $1 million net worth or particularly complex plans. Special does not include drafting trusts. Available to Maryland residents only.</p>
    </div>
  </article>

  <article class="panel panel--2">
    <div class="attorney-bg"></div>
    <div class="portrait" role="img" aria-label="Portrait photo of the attorney"></div>
    <svg class="shapes" viewBox="0 0 247 572" preserveAspectRatio="none" aria-hidden="true">
      <polygon points="48,176 48,160 82,176" fill="var(--gold)"/>
      <polygon points="198,138 198,176 120,176" fill="var(--gold)"/>
    </svg>
    <p class="txt quote">“ I’ve seen first-hand the problems created when a parent dies without a will. Young parents are least likely to think about estate planning, but having a plan for a guardian is most important when your children are small. I created our estate planning special to encourage new parents to start planning before it’s too late.”</p>
    <p class="txt attorney-name">Dana R. Hollis, Esq.</p>
    <div class="txt firm">
      <div class="firm-name"><span class="mark"></span>HOLLIS LEGAL, LLC</div>
      <p class="address">415 E. Maple Avenue, Suite 310,<br>Towson, MD 21204</p>
      <p>P: (410)-555-0148 F: (410)-555-0172</p>
      <p>E: dana@hollis-legal.example</p>
      <p>www.hollis-legal.example</p>
    </div>
  </article>

  <article class="panel panel--3">
    <div class="cover-bg"></div>
    <div class="photo photo--family" role="img" aria-label="Photo of young parents smiling with their baby"></div>
    <svg class="shapes" viewBox="0 0 247 572" preserveAspectRatio="none" aria-hidden="true">
      <polygon points="247,205 247,290 130,290" fill="var(--gold)"/>
      <polygon points="0,290 247,290 247,302 123,332 0,302" fill="var(--slate)"/>
      <polygon points="0,302 0,338 62,317" fill="var(--gold)"/>
    </svg>
    <div class="txt cover-title">
      <h1>ESTATE PLANNING SPECIAL<br><span class="highlight">FOR NEW PARENTS</span></h1>
      <p>For parents-to-be and parents of children<br>under 5 years old.</p>
    </div>
  </article>
</section>

<!-- Inside of the sheet -->
<section class="sheet sheet--inside">
  <article class="panel panel--1">
    <div class="photo photo--scales" role="img" aria-label="Photo of brass scales of justice on a desk"></div>
    <svg class="shapes" viewBox="0 0 247 572" preserveAspectRatio="none" aria-hidden="true">
      <polygon points="0,212 247,212 247,216 0,232" fill="#fff"/>
      <polygon points="0,548 247,540 247,572 0,572" fill="var(--brown)"/>
      <polygon points="0,506 0,572 118,572" fill="var(--gold)"/>
    </svg>
    <div class="txt why">
      <h3>Why should every parent have a will?</h3>
      <p>Imagine how many people love your children. Would there be a fight over who would care for your children if you passed away without leaving instructions?</p>
      <p>Naming a guardian in your will helps avoid litigation that would cause additional stress to your children and loved ones. You can also name a back-up in the event that your first choice is unable or unwilling to serve as guardian.</p>
      <h3>What happens if I die in Maryland without a will?</h3>
      <p>If you are married and have minor children, your spouse will inherit one half of your intestate property and your children will inherit the rest. If you have children but no spouse, your children will inherit everything.</p>
    </div>
  </article>

  <article class="panel panel--2">
    <svg class="shapes" viewBox="0 0 247 572" preserveAspectRatio="none" aria-hidden="true">
      <polygon points="0,212 247,196 247,322 0,352" fill="var(--gold)"/>
      <polygon points="0,352 247,322 247,336 0,368" fill="var(--brown)"/>
      <polygon points="0,540 247,532 247,572 0,572" fill="var(--brown)"/>
    </svg>
    <div class="txt laws-intro">
      <p>For most parents, this plan doesn’t make sense. Married people generally want their spouse to inherit all of their estate and unmarried people should have more control over how funds are distributed to their minor children.</p>
      <p>Furthermore, Maryland law doesn’t take into account nontraditional families. For example, foster children and stepchildren that are not legally adopted will not automatically inherit a share of your estate.</p>
    </div>
    <p class="txt laws-callout">You can find the complete laws of intestacy (dying without a will) in the Maryland Code of Estates &amp; Trusts §§ 3-101 to 3-303.</p>
    <div class="txt later">
      <h3>Should we prepare a will now if we plan to have more children in the future?</h3>
      <p>There is no reason to put off drafting a will. A will can be written to treat your children as a “class” that would include any future children born to or adopted by you.</p>
    </div>
    <p class="txt call"><span class="label">Call Now</span>(410)-555-0148</p>
  </article>

  <article class="panel panel--3">
    <div class="cover-bg"></div>
    <div class="photo photo--signing" role="img" aria-label="Photo of a hand signing a last will and testament"></div>
    <svg class="shapes" viewBox="0 0 247 572" preserveAspectRatio="none" aria-hidden="true">
      <polygon points="0,150 247,118 247,160 0,172" fill="var(--brown)"/>
    </svg>
    <div class="txt process">
      <h3>What does the estate planning package include?</h3>
      <p>Our estate planning package includes a will, an advance medical directive, and a power of attorney. A will names a guardian for your children and gives instructions on how to distribute your probate property at death. An advance medical directive, also known as a living will, states directions regarding your healthcare decisions in the event that you can’t make those decisions yourself. A power of attorney gives someone the ability to handle your financial affairs during your lifetime.</p>
      <h3>How long will the process take?</h3>
      <p>Before our first meeting, you will receive information to help you start thinking about some of the decisions we’ll make during the initial consultation which lasts approximately one hour. It takes about 2 to 3 weeks after our initial meeting to draft your documents. You will receive draft copies of your documents to review before coming in for your last appointment to sign the documents in front of witnesses and a notary.</p>
    </div>
  </article>
</section>

</body>
</html>
```